Update Product Descriptions on Existing Website

We need to update product descriptions and images on three pages of our existing website. The tables are in editable HTML format. The formatting will be the exact same, just need the descriptions and images updated.

I have included the source documents below.

Coding

Coded - Design and coding required

Number of Pages Required

3 page

Colors

Designer to choose colors to be used in the design.

```html
<!DOCTYPE html>
<html lang="en">
<head>
<meta charset="utf-8">
<title>Pultruded Grating Sizes and Types</title>
<link href="https://fonts.googleapis.com/css2?family=Tinos:wght@400&display=swap" rel="stylesheet">
<style>
  :root {
    --page-bg: #ffffff;
    --ink: #000000;
    --rule: #222222;
    --grate-dark: #0e7a3a;
    --grate-mid: #1f9a4c;
    --grate-light: #35b062;
  }
  html, body {
    margin: 0;
    padding: 0;
    width: 934px;
    height: 1200px;
    overflow: hidden;
    background: var(--page-bg);
    color: var(--ink);
    font-family: "Tinos", "Times New Roman", serif;
  }
  .intro {
    margin: 0;
    padding: 3px 0 0 10px;
    font-size: 17.5px;
    line-height: 22px;
  }
  .grating-table {
    margin-left: 10px;
    width: 906px;
    border-collapse: collapse;
    table-layout: fixed;
    font-size: 17px;
    line-height: 20px;
  }
  .grating-table col.label-col { width: 258px; }
  .grating-table td {
    border: 1.5px solid var(--rule);
    padding: 0 2px;
    height: 20px;
    vertical-align: middle;
    white-space: nowrap;
  }
  .grating-table tr.profile-row td { height: 153px; }
  .profile-cell { text-align: center; }
  .profile-shape {
    display: inline-block;
    width: 136px;
    height: 96px;
    border-radius: 4px;
    background: linear-gradient(160deg, var(--grate-light), var(--grate-mid) 50%, var(--grate-dark));
    vertical-align: middle;
  }
  .profile-shape.tall { height: 112px; width: 120px; }
</style>
</head>
<body>
<p class="intro">The following sizes and types of pultruded grating are available from Northbar:</p>
<table class="grating-table">
  <colgroup><col class="label-col"><col><col><col><col></colgroup>

  <tr class="profile-row">
    <td>Profile Image (click to enlarge)</td>
    <td class="profile-cell"><span class="profile-shape" role="img" aria-label="Isometric profile drawing of T4010 grating"></span></td>
    <td class="profile-cell"><span class="profile-shape" role="img" aria-label="Isometric profile drawing of T5010 grating"></span></td>
    <td class="profile-cell"><span class="profile-shape" role="img" aria-label="Isometric profile drawing of T6010 grating"></span></td>
    <td class="profile-cell"><span class="profile-shape" role="img" aria-label="Isometric profile drawing of I4010 grating"></span></td>
  </tr>
  <tr><td>Type</td><td>T4010</td><td>T5010</td><td>T6010</td><td>I4010</td></tr>
  <tr><td>Height (in.)</td><td>1</td><td>1</td><td>1</td><td>1</td></tr>
  <tr><td>Standard Panel Width (ft.)</td><td>3,4</td><td>3,4</td><td>3,4</td><td>3,4</td></tr>
  <tr><td>Standard Panel Length (ft.)</td><td>8,10,12,20</td><td>8,10,12,20</td><td>8,10,12,20</td><td>8,10,12,20</td></tr>
  <tr><td>Open Area</td><td>40%</td><td>50%</td><td></td><td>40%</td></tr>
  <tr><td>Weight (lbs./ft.)</td><td>2.46</td><td>2.15</td><td>1.74</td><td>3.28</td></tr>

  <tr class="profile-row">
    <td>Profile Image (click to enlarge)</td>
    <td class="profile-cell"><span class="profile-shape" role="img" aria-label="Isometric profile drawing of I5010 grating"></span></td>
    <td class="profile-cell"><span class="profile-shape" role="img" aria-label="Isometric profile drawing of I6010 grating"></span></td>
    <td class="profile-cell"><span class="profile-shape" role="img" aria-label="Isometric profile drawing of I4012 grating"></span></td>
    <td class="profile-cell"><span class="profile-shape" role="img" aria-label="Isometric profile drawing of II5012 grating"></span></td>
  </tr>
  <tr><td>Type</td><td>I5010</td><td>I6010</td><td>I4012</td><td>II5012</td></tr>
  <tr><td>Height (in.)</td><td>1</td><td>1</td><td>1.25</td><td>1.25</td></tr>
  <tr><td>Standard Panel Width (ft.)</td><td>3,4</td><td>3,4</td><td>3,4</td><td>3,4</td></tr>
  <tr><td>Standard Panel Length (ft.)</td><td>8,10,12,20</td><td>8,10,12,20</td><td>8,10,12,20</td><td>8,10,12,20</td></tr>
  <tr><td>Open Area</td><td>50%</td><td>60%</td><td>40%</td><td>50%</td></tr>
  <tr><td>Weight (lbs./ft.)</td><td>2.74</td><td>2.21</td><td>4.12</td><td>3.48</td></tr>

  <tr class="profile-row">
    <td>Profile Image (click to enlarge)</td>
    <td class="profile-cell"><span class="profile-shape" role="img" aria-label="Isometric profile drawing of I6012 grating"></span></td>
    <td class="profile-cell"><span class="profile-shape" role="img" aria-label="Isometric profile drawing of I4015 grating"></span></td>
    <td class="profile-cell"><span class="profile-shape" role="img" aria-label="Isometric profile drawing of I5015 grating"></span></td>
    <td class="profile-cell"><span class="profile-shape" role="img" aria-label="Isometric profile drawing of I6015 grating"></span></td>
  </tr>
  <tr><td>Type</td><td>I6012</td><td>I4015</td><td>I5015</td><td>I6015</td></tr>
  <tr><td>Height (in.)</td><td>1.25</td><td>1.5</td><td>1.5</td><td>1.5</td></tr>
  <tr><td>Standard Panel Width (ft.)</td><td>3,4</td><td>3,4</td><td>3,4</td><td>3,4</td></tr>
  <tr><td>Standard Panel Length (ft.)</td><td>8,10,12,20</td><td>8,10,12,20</td><td>8,10,12,20</td><td>8,10,12,20</td></tr>
  <tr><td>Open Area</td><td>60%</td><td>40%</td><td>50%</td><td>60%</td></tr>
  <tr><td>Weight (lbs./ft.)</td><td>2.89</td><td>5.33</td><td>4.57</td><td>3.71</td></tr>

  <tr class="profile-row">
    <td>Profile Image (click to enlarge)</td>
    <td class="profile-cell"><span class="profile-shape tall" role="img" aria-label="Isometric profile drawing of T3320 grating"></span></td>
    <td class="profile-cell"><span class="profile-shape tall" role="img" aria-label="Isometric profile drawing of T5020 grating"></span></td>
    <td class="profile-cell"><span class="profile-shape tall" role="img" aria-label="Isometric profile drawing of T3330 grating"></span></td>
    <td class="profile-cell"><span class="profile-shape tall" role="img" aria-label="Isometric profile drawing of T5030 grating"></span></td>
  </tr>
  <tr><td>Type</td><td>T3320</td><td>T5020</td><td>T3330</td><td>T5030</td></tr>
  <tr><td>Height (in.)</td><td>2</td><td>2</td><td>3</td><td>3</td></tr>
  <tr><td>Standard Panel Width (ft.)</td><td>3,4</td><td>3,4</td><td>3,4</td><td>3,4</td></tr>
  <tr><td>Standard Panel Length (ft.)</td><td>8,10,12,20</td><td>8,10,12,20</td><td>8,10,12,20</td><td>8,10,12,20</td></tr>
  <tr><td>Open Area</td><td>33%</td><td>50%</td><td>33%</td><td>50%</td></tr>
  <tr><td>Weight (lbs./ft.)</td><td>4.63</td><td>3.56</td><td>5.21</td><td>6.8</td></tr>
</table>
</body>
</html>
```